Brochure design for HVAC Company

A classic tri-fold brochure design for an air conditioning, refrigeration, and heating company. Would like the designs to be simple (uncluttered), professional, and pull in the logo colors. Attached is the logo and a business card designs. The company name is Steady Breeze Air Conditioning, Refrigeration, and Heating.

Target Market(s)

Businesses normally food establishments for refrigeration and ice machines. Looking to sell them on maintenance plan: Gold, Silver, and Bronze. The material should help them to understand the services offered: Maintenance, Servicing and Troubleshooting, and Installations of ice machines, commercial refrigeration, and walk-in freezers and air conditioning (duct, ductless, and rooftop)

Industry/Entity Type

Hvac

Font styles to use
Sans Serif

Requirements
Must have
• Include standard information, such as company name, at least two types of contact information (phone, email and post office address), a logo and tagline. It should also include a headline on the front and two or three brief items outlining benefits your organization can provide.
• Tagline is approximately 14 words and 66 characters.
• Looking to inform customers of services offered: maintenance three plans gold, silver, and bronze, servicing and troubleshooting, and installation.
• Products Serviced, maintained, and installed: Commercial refrigeration, Ice Machines, Air Conditioning (both duct, ductless, and rooftop), walk in freezers.
• Call to action is $100 off on signed maintenance contract. $50 off on first service call.
• Use lorem ipsum text to complement the details of the above information. I will add it later before printing.
• Use logo color scheme and any other colors that complement it.
• Would like this to be a word template.
Nice to have
• Can you make this a Microsoft Word template? Sketch is good, or adobe cs4 format.
Should not have
• Photos should NOT be focused on the homeowner. Should BE focused on the commercial side of the business. Photos can be from any of these product areas: commercial refrigeration, ice machine, walk in freezer boxes, and light roof top ac and heating units.

```html
<!DOCTYPE html>
<html lang="en">
<head>
<meta charset="utf-8">
<title>Steady Breeze – Maintenance Plans &amp; Products</title>
<link rel="stylesheet" href="https://fonts.googleapis.com/css2?family=Mulish:ital,wght@0,400;0,700;0,800;1,300&display=swap">
<style>
  :root {
    --blue: #2341f4;
    --orange: #ff4b06;
    --white: #ffffff;
    --panel-grey: #f1f1f1;
    --rule: #1a1a1a;
    --photo-steel: #8f979c;
    --photo-cool: #c9d3cf;
    --photo-ice: #c9342e;
    --photo-white: #e4e6e8;
  }
  * { box-sizing: border-box; margin: 0; padding: 0; }
  html, body { width: 1200px; height: 848px; overflow: hidden; background: var(--white); }
  body { font-family: "Mulish", sans-serif; }

  .brochure { position: relative; width: 1200px; height: 848px; overflow: hidden; background: var(--blue); }

  /* Plans strip */
  .plans { position: absolute; left: 0; top: 0; width: 1200px; height: 284px; background: var(--white); display: flex; border-top: 1px solid var(--rule); }
  .plan { position: relative; width: 400px; height: 100%; border-left: 1px solid var(--rule); }
  .plan-badge { position: absolute; top: 16px; width: 102px; height: 102px; border-radius: 50%; display: flex; align-items: center; justify-content: center; font-weight: 800; letter-spacing: -0.5px; }
  .plan--gold .plan-badge { left: 141px; background: var(--blue); color: var(--orange); font-size: 36px; }
  .plan--bronze .plan-badge { left: 149px; background: var(--orange); color: var(--blue); font-size: 28px; }
  .plan--silver .plan-badge { left: 194px; background: var(--blue); color: var(--white); font-size: 36px; border: 6px solid var(--orange); }
  .plan-copy { position: absolute; top: 132px; font-style: italic; font-weight: 300; font-size: 29px; line-height: 34.5px; white-space: nowrap; }
  .plan--gold .plan-copy { left: 121px; color: var(--blue); }
  .plan--bronze .plan-copy { left: 94px; color: var(--orange); }
  .plan--silver .plan-copy { left: 87px; color: var(--blue); }

  .maintenance-mark { position: absolute; left: 0; top: 0; width: 120px; height: 284px; }
  .maintenance-mark .tool-art { position: absolute; left: 14px; top: 150px; width: 98px; height: 124px; background: var(--orange); }
  .maintenance-mark .word { position: absolute; font-size: 17px; font-weight: 400; color: var(--rule); transform: rotate(-90deg); transform-origin: left top; white-space: nowrap; }
  .maintenance-mark .word--maint { left: 60px; top: 216px; }
  .maintenance-mark .word--plans { left: 60px; top: 62px; }
  .maintenance-mark .numeral { position: absolute; left: 40px; top: 50px; font-size: 66px; font-weight: 800; color: var(--orange); transform: rotate(-90deg); line-height: 1; }

  /* Bands */
  .band { position: absolute; left: 0; width: 1200px; background: var(--orange); }
  .band--top { top: 284px; height: 20px; }
  .band--bottom { top: 682px; height: 98px; }

  .products-heading { position: absolute; left: 26px; top: 316px; width: 358px; height: 119px; background: var(--panel-grey); color: var(--orange); font-weight: 800; font-size: 28px; line-height: 34.5px; text-align: center; padding-top: 6px; }

  .curved-labels { position: absolute; left: 0; top: 0; width: 1200px; height: 848px; z-index: 2; }
  .curved-labels text { font-family: "Mulish", sans-serif; font-weight: 400; }

  .photo { position: absolute; }
  .photo--ac { left: 530px; top: 400px; width: 130px; height: 124px; background: linear-gradient(180deg, #6b7479, #3f474b 60%, var(--photo-steel)); }
  .photo--walkin { left: 900px; top: 412px; width: 214px; height: 176px; background: linear-gradient(135deg, #e8ebe3, var(--photo-cool) 45%, #b9c7a8); }
  .photo--ice-maker { left: 88px; top: 576px; width: 144px; height: 192px; background: linear-gradient(90deg, #d7d9db, var(--photo-white) 40%, #2a2a2a 85%); }
  .photo--ice-kiosk { left: 484px; top: 565px; width: 180px; height: 261px; background: linear-gradient(180deg, var(--photo-ice) 0%, #c2404a 28%, #8d9397 30%, #2f4fd8 70%, #d9e1ea 100%); }

  .walkin-copy { position: absolute; left: 888px; top: 598px; color: var(--white); font-style: italic; font-weight: 300; font-size: 29px; line-height: 34.5px; white-space: nowrap; }

  .signature { position: absolute; left: 1046px; top: 788px; display: flex; align-items: center; gap: 8px; }
  .signature .dot { width: 30px; height: 30px; border-radius: 50%; background: var(--orange); }
  .signature .name { color: var(--white); font-weight: 800; font-size: 17px; line-height: 19px; text-transform: uppercase; }
</style>
</head>
<body>
<main class="brochure">

  <section class="plans">
    <div class="plan plan--gold">
      <div class="maintenance-mark">
        <div class="tool-art" role="img" aria-label="Orange wrench illustration"></div>
        <span class="numeral">3</span>
        <span class="word word--maint">maintenance</span>
        <span class="word word--plans">plans</span>
      </div>
      <div class="plan-badge">Gold</div>
      <p class="plan-copy">lorum ipsum lorum<br>ipsum lorum ipsum<br>lorum ipsum lorum<br>ipsum lorum ipsum</p>
    </div>
    <div class="plan plan--bronze">
      <div class="plan-badge">Bronze</div>
      <p class="plan-copy">lorum ipsum lorum<br>ipsum lorum ipsum<br>lorum ipsum lorum<br>ipsum lorum ipsum</p>
    </div>
    <div class="plan plan--silver">
      <div class="plan-badge">silver</div>
      <p class="plan-copy">lorum ipsum lorum<br>ipsum lorum ipsum<br>lorum ipsum lorum<br>ipsum lorum ipsum</p>
    </div>
  </section>

  <div class="band band--top"></div>
  <div class="band band--bottom"></div>

  <h2 class="products-heading">Products Serviced,<br>maintained, and in-<br>stalled</h2>

  <div class="photo photo--ac" role="img" aria-label="Photo of an outdoor air conditioning condenser unit"></div>
  <div class="photo photo--walkin" role="img" aria-label="Photo of a walk-in freezer with glass display doors stocked with drinks"></div>
  <div class="photo photo--ice-maker" role="img" aria-label="Photo of an undercounter commercial ice maker with its door open"></div>
  <div class="photo photo--ice-kiosk" role="img" aria-label="Photo of a bagged ice vending kiosk"></div>

  <svg class="curved-labels" viewBox="0 0 1200 848" aria-hidden="true">
    <defs>
      <path id="arc-commercial" d="M30 586 Q184 430 340 592"/>
      <path id="arc-air" d="M496 404 Q600 334 710 408"/>
      <path id="arc-walkin" d="M908 398 Q1012 334 1114 406"/>
      <path id="arc-ice" d="M470 560 Q570 522 670 560"/>
    </defs>
    <text fill="var(--white)" font-size="30"><textPath href="#arc-commercial" startOffset="50%" text-anchor="middle">Commercial refrigeration</textPath></text>
    <text fill="var(--orange)" font-size="27"><textPath href="#arc-air" startOffset="50%" text-anchor="middle">Air Conditioning</textPath></text>
    <text fill="var(--white)" font-size="27"><textPath href="#arc-walkin" startOffset="50%" text-anchor="middle">walk in freezers</textPath></text>
    <text fill="var(--orange)" font-size="28"><textPath href="#arc-ice" startOffset="50%" text-anchor="middle">Ice Machine</textPath></text>
  </svg>

  <p class="walkin-copy">lorum ipsum lorum<br>ipsum lorum ipsum</p>

  <div class="signature">
    <span class="dot"></span>
    <span class="name">Steady<br>Breeze</span>
  </div>

</main>
</body>
</html>
```